Valmo Sàrl - Business Card

VALMO Sàrl operates in the sector Services for banks and credit institutions. It is a B2B which connects companies. The main colors should be Blue and Black. The logo and look of the card should be simple, professional, conservative and reflect Connecting People.

Target Market(s)

Financial professionals and institutions

Industry/Entity Type

Finance

Contact Information for Business Card

Chemin des Vergers 9
1026 Denges

Logo Text

Connecting dots

Font styles to use
Serif
Sans Serif

Colors
0355a3
3176b5
85acd3
cfdeed

Requirements
Should not have
• Multiple colors

```html
<!DOCTYPE html>
<html lang="en">
<head>
<meta charset="utf-8">
<title>Valmo Sàrl – Business Card</title>
<link href="https://fonts.googleapis.com/css2?family=Montserrat:wght@600&family=Arimo:wght@400;700&display=swap" rel="stylesheet">
<style>
  :root {
    --blue-deep: #0355a3;
    --blue-mid: #3176b5;
    --blue-light: #85acd3;
    --blue-pale: #cfdeed;
    --ink: #1a1a1a;
    --grey: #3a3a3a;
    --paper: #ffffff;
    --backdrop: #e9ebee;
  }
  * { box-sizing: border-box; margin: 0; padding: 0; }
  html, body {
    width: 1189px; height: 1200px; overflow: hidden;
    background: var(--backdrop);
  }
  .canvas { position: relative; width: 1189px; height: 1200px; }

  .card {
    position: absolute; left: 170px; width: 850px;
    background: var(--paper); border-radius: 28px; overflow: hidden;
    box-shadow: 0 6px 18px rgba(0,0,0,.18);
  }
  .card--front { top: 112px; height: 484px; }
  .card--back { top: 641px; height: 486px; }

  .brand-dot {
    position: absolute; border-radius: 50%; background: var(--blue-deep);
  }
  .brand-name {
    position: absolute; white-space: nowrap;
    font-family: "Montserrat", sans-serif; font-weight: 600;
    color: var(--blue-deep); letter-spacing: -0.5px;
  }

  .card--front .brand-dot { left: 118px; top: 62px; width: 134px; height: 134px; }
  .card--front .brand-name { left: 46px; top: 213px; font-size: 56px; }

  .faint-disc {
    position: absolute; left: 460px; top: -60px; width: 400px; height: 400px;
    border-radius: 50%; background: var(--blue-pale); opacity: .45;
  }

  .holder { position: absolute; right: 44px; top: 74px; text-align: right; }
  .holder__name {
    font-family: "Montserrat", sans-serif; font-weight: 600;
    font-size: 29px; color: var(--blue-deep);
  }
  .holder__role {
    font-family: "Arimo", sans-serif; font-size: 21px; color: var(--grey); margin-top: 2px;
  }

  .divider {
    position: absolute; left: 49px; right: 44px; top: 352px;
    height: 2px; background: var(--blue-deep);
  }

  .contacts {
    position: absolute; left: 49px; top: 363px; list-style: none;
    font-family: "Arimo", sans-serif; font-size: 20px; color: var(--ink);
  }
  .contacts li { display: flex; align-items: center; height: 31px; }
  .contacts svg { width: 21px; height: 21px; margin-right: 12px; flex: none; }

  .address {
    position: absolute; right: 44px; top: 364px; text-align: right;
    font-family: "Arimo", sans-serif; font-size: 20px; color: var(--ink); line-height: 28px;
  }
  .address__web { margin-top: 4px; }
  .address__web b { color: var(--blue-deep); font-weight: 700; }

  .base-band {
    position: absolute; left: 0; right: 0; bottom: 0; height: 12px; background: var(--blue-deep);
  }

  .card--back .brand-dot { left: 360px; top: 140px; width: 130px; height: 130px; }
  .card--back .brand-name {
    left: 0; right: 0; top: 298px; text-align: center; font-size: 60px;
  }
</style>
</head>
<body>
<main class="canvas">

  <section class="card card--front" aria-label="Business card front">
    <div class="faint-disc" aria-hidden="true"></div>
    <div class="brand-dot" aria-hidden="true"></div>
    <div class="brand-name">Valmo Sàrl</div>

    <div class="holder">
      <div class="holder__name">Claire Morel</div>
      <div class="holder__role">Manager</div>
    </div>

    <div class="divider"></div>

    <ul class="contacts">
      <li>
        <svg viewBox="0 0 24 24" aria-hidden="true"><circle cx="12" cy="12" r="12" fill="var(--blue-deep)"/><path d="M9 6.5l2 2.8-1.3 1.3c.7 1.6 2 2.9 3.6 3.6l1.3-1.3 2.8 2-1 2c-4.5-.3-8.3-4.1-8.6-8.6z" fill="#fff"/></svg>
        (021) 555 0142
      </li>
      <li>
        <svg viewBox="0 0 24 24" aria-hidden="true"><circle cx="12" cy="12" r="12" fill="var(--blue-deep)"/><rect x="8.5" y="6" width="7" height="3.5" fill="#fff"/><rect x="6" y="10" width="12" height="5" rx="1" fill="#fff"/><rect x="8.5" y="14" width="7" height="4" fill="#fff" stroke="var(--blue-deep)" stroke-width=".8"/></svg>
        (021) 555 0143
      </li>
      <li>
        <svg viewBox="0 0 24 24" aria-hidden="true"><circle cx="12" cy="12" r="12" fill="var(--blue-deep)"/><rect x="6" y="8" width="12" height="8.5" fill="#fff"/><path d="M6 8l6 5 6-5" fill="none" stroke="var(--blue-deep)" stroke-width="1.2"/></svg>
        info@valmosarl.ch
      </li>
    </ul>

    <div class="address">
      <div>Chemin des Vergers 9</div>
      <div>1026 Denges</div>
      <div class="address__web">www.<b>valmosarl</b>.ch</div>
    </div>

    <div class="base-band"></div>
  </section>

  <section class="card card--back" aria-label="Business card back">
    <div class="brand-dot" aria-hidden="true"></div>
    <div class="brand-name">Valmo Sàrl</div>
  </section>

</main>
</body>
</html>
```